Asset tracing and investigation firm requires marketing brochure for services

We need a professional looking brochure with layout that supports the text that we have already drafted, is easy on the eye and can easily be navigated by clients either electronic/screen format or printed format. The wording is not finalised and all aspects need to be remain editable (including the logo and picture(s)) - preferably in Word or similarly accessible format.

```html
<!DOCTYPE html>
<html lang="en">
<head>
<meta charset="utf-8">
<title>Verant Asset Tracing Services Brochure</title>
<link rel="stylesheet" href="https://fonts.googleapis.com/css2?family=Montserrat:wght@400;600;700;800&family=Open+Sans:wght@400;600&display=swap">
<style>
:root{
  --stage:#d8d8da;
  --paper:#ffffff;
  --blue:#2f5fae;
  --blue-dark:#1f3f86;
  --blue-soft:#6f98cf;
  --blue-pale:#b9cce6;
  --yellow:#e8b531;
  --teal:#8cc3cf;
  --ink:#3a3d44;
  --grey:#8a8d93;
}
*{box-sizing:border-box;margin:0;padding:0}
html,body{width:1200px;height:3608px;overflow:hidden;background:#fff}
body{font-family:"Open Sans",Arial,sans-serif;color:var(--ink)}
.stage{height:902px;background:var(--stage);display:flex;align-items:center;justify-content:center;border-top:3px solid #fff}
.stage:first-child{border-top:0}
.page{position:relative;background:var(--paper);box-shadow:0 18px 30px rgba(0,0,0,.18);overflow:hidden}
.page svg.art{position:absolute;inset:0;width:100%;height:100%}
.spread{display:flex;box-shadow:0 18px 30px rgba(0,0,0,.18)}
.spread .page{box-shadow:none}
.spread .page+.page{border-left:1px solid #e2e2e2}
.heading{font-family:"Montserrat",Arial,sans-serif}
.brand{font-family:"Montserrat",Arial,sans-serif;font-weight:700;color:var(--blue)}
.brand::before{content:"";display:inline-block;width:.6em;height:.6em;background:var(--yellow);margin-right:.3em;vertical-align:.05em}
/* inner pages */
.inner{width:500px;height:342px}
.blk{position:absolute;font-size:5.6px;line-height:1.5;color:var(--ink)}
.blk h3{font-family:"Montserrat",Arial,sans-serif;font-size:8px;font-weight:800;color:var(--blue);margin-bottom:4px}
.blk h3 span{color:var(--yellow)}
.blk p{margin-bottom:4px}
.icon{display:inline-block;width:9px;height:9px;border-radius:2px;background:var(--ink);margin-right:4px;vertical-align:-1px}
.side-band{position:absolute;left:0;top:0;bottom:0;width:30px}
.side-url{position:absolute;left:6px;top:18px;writing-mode:vertical-rl;transform:rotate(180deg);font-family:"Montserrat",Arial,sans-serif;font-size:6px;font-weight:700;color:#fff}
.foot-band{position:absolute;left:0;right:0;bottom:0;height:26px}
.foot-url{position:absolute;right:18px;bottom:7px;font-family:"Montserrat",Arial,sans-serif;font-size:6px;font-weight:700;color:#fff}
.page-no{position:absolute;bottom:26px;width:22px;height:14px;background:var(--yellow);color:#fff;font-family:"Montserrat",Arial,sans-serif;font-size:6.5px;font-weight:700;display:flex;align-items:center;justify-content:center}
.num{display:flex;gap:6px;align-items:flex-start;margin-bottom:5px}
.num b{flex:none;width:12px;height:12px;border-radius:50%;background:var(--yellow);color:#fff;font-size:6px;display:flex;align-items:center;justify-content:center}
/* table */
.tier-table{position:absolute;left:22px;top:40px;width:456px;border-collapse:collapse;font-size:5.2px;line-height:1.45}
.tier-table th{background:var(--blue);color:#fff;font-family:"Montserrat",Arial,sans-serif;font-weight:700;padding:5px 4px;text-align:left}
.tier-table td{padding:5px 4px;vertical-align:top;border-bottom:1px solid #d6dde6;height:38px}
.tier-table td.shade{background:linear-gradient(180deg,#a9d2db,#6fb0bf);color:#23414a}
.tier-table td.shade2{background:linear-gradient(180deg,#bfe0e7,#8cc3cf);color:#23414a}
.tier-table tfoot td{background:#1d2430;color:#fff;height:12px;padding:3px 4px;font-weight:600}
.portrait{position:absolute;left:270px;top:62px;width:54px;height:62px;background:linear-gradient(180deg,#e8ecf1,#9aa3b0);border:1px solid #c9ced6}
</style>
</head>
<body>

<!-- Stage 1: front cover -->
<section class="stage">
  <article class="page cover" style="width:760px;height:520px">
    <svg class="art" viewBox="0 0 760 520" aria-hidden="false">
      <defs>
        <linearGradient id="band" x1="0" x2="1">
          <stop offset="0" stop-color="#e8b531"/><stop offset=".56" stop-color="#e8b531"/>
          <stop offset=".56" stop-color="#2f5fae"/><stop offset="1" stop-color="#2f5fae"/>
        </linearGradient>
        <linearGradient id="sky" x1="0" y1="1" x2="1" y2="0">
          <stop offset="0" stop-color="#d9d4cb"/><stop offset=".3" stop-color="#2c5b9c"/>
          <stop offset=".6" stop-color="#8fb6e0"/><stop offset="1" stop-color="#b8bdc4"/>
        </linearGradient>
      </defs>
      <polygon points="0,52 760,0 760,22 0,74" fill="url(#band)"/>
      <polygon points="0,74 760,22 760,240 0,330" fill="url(#sky)" role="img" aria-label="Photograph of glass City of London office towers against a blue sky"/>
      <polygon points="0,330 760,240 760,246 0,336" fill="#fff"/>
      <line x1="40" y1="420" x2="150" y2="420" stroke="#2f5fae" stroke-width="2"/>
      <text x="40" y="368" font-family="Montserrat, sans-serif" font-size="22" font-weight="600" fill="#e8b531">VERANT -ASSET</text>
      <text x="40" y="400" font-family="Montserrat, sans-serif" font-size="30" font-weight="800" fill="#2f5fae">TRACING SERVICES</text>
      <text x="40" y="446" font-family="Montserrat, sans-serif" font-size="14" font-weight="700" fill="#1f2a3a">www.verant.co.uk</text>
      <rect x="596" y="280" width="14" height="14" fill="#e8b531"/>
      <text x="616" y="294" font-family="Montserrat, sans-serif" font-size="24" font-weight="700" fill="#2f5fae">VERANT</text>
    </svg>
  </article>
</section>

<!-- Stage 2: back and front cover spread -->
<section class="stage">
  <div class="spread">
    <article class="page back-cover" style="width:460px;height:315px">
      <svg class="art" viewBox="0 0 460 315">
        <rect x="200" y="0" width="260" height="150" fill="#eef0f3" role="img" aria-label="Faint photograph of a classical stone building"/>
        <polygon points="120,38 460,0 460,12 120,50" fill="#e8b531"/>
        <polygon points="0,236 120,182 120,196 0,250" fill="#2f5fae"/>
        <g>
          <rect x="150" y="60" width="26" height="26" fill="#b9cce6"/>
          <rect x="118" y="92" width="26" height="26" fill="#6f98cf"/>
          <rect x="150" y="92" width="26" height="26" fill="#b9cce6"/>
          <rect x="86" y="124" width="26" height="26" fill="#2f5fae"/>
          <rect x="118" y="124" width="26" height="26" fill="#2f5fae"/>
          <rect x="150" y="124" width="26" height="26" fill="#6f98cf"/>
          <rect x="54" y="156" width="26" height="26" fill="#e8b531"/>
          <rect x="86" y="156" width="26" height="26" fill="#e8b531"/>
          <rect x="118" y="156" width="26" height="26" fill="#e8b531"/>
          <rect x="150" y="156" width="26" height="26" fill="#f0cc6a"/>
        </g>
        <rect x="282" y="58" width="8" height="8" fill="#e8b531"/>
        <text x="294" y="66" font-family="Montserrat, sans-serif" font-size="12" font-weight="700" fill="#2f5fae">VERANT</text>
        <text x="214" y="96" font-family="Montserrat, sans-serif" font-size="9" font-weight="800" fill="#2f5fae">CONTACT US</text>
        <circle cx="218" cy="114" r="3.5" fill="#2f5fae"/>
        <text x="226" y="117" font-family="Open Sans, sans-serif" font-size="7" font-weight="600" fill="#3a3d44">0207 555 0148</text>
        <rect x="214.5" y="127" width="7" height="5" fill="#2f5fae"/>
        <text x="226" y="132" font-family="Open Sans, sans-serif" font-size="7" fill="#3a3d44">enquiries@verant.co.uk</text>
        <circle cx="218" cy="144" r="3.5" fill="#2f5fae"/>
        <text x="226" y="147" font-family="Open Sans, sans-serif" font-size="7" fill="#3a3d44">www.verant.co.uk</text>
        <path d="M170 200 Q320 170 460 120" stroke="#2f5fae" stroke-width="1.2" fill="none"/>
      </svg>
    </article>
    <article class="page cover" style="width:460px;height:315px">
      <svg class="art" viewBox="0 0 760 520">
        <polygon points="0,52 760,0 760,22 0,74" fill="url(#band)"/>
        <polygon points="0,74 760,22 760,240 0,330" fill="url(#sky)" role="img" aria-label="Photograph of glass City of London office towers against a blue sky"/>
        <line x1="40" y1="420" x2="150" y2="420" stroke="#2f5fae" stroke-width="2"/>
        <text x="40" y="368" font-family="Montserrat, sans-serif" font-size="22" font-weight="600" fill="#e8b531">VERANT -ASSET</text>
        <text x="40" y="400" font-family="Montserrat, sans-serif" font-size="30" font-weight="800" fill="#2f5fae">TRACING SERVICES</text>
        <text x="40" y="446" font-family="Montserrat, sans-serif" font-size="14" font-weight="700" fill="#1f2a3a">www.verant.co.uk</text>
        <rect x="596" y="280" width="14" height="14" fill="#e8b531"/>
        <text x="616" y="294" font-family="Montserrat, sans-serif" font-size="24" font-weight="700" fill="#2f5fae">VERANT</text>
      </svg>
    </article>
  </div>
</section>

<!-- Stage 3: inner spread, about and reports -->
<section class="stage">
  <div class="spread">
    <article class="page inner">
      <svg class="side-band" viewBox="0 0 30 342" preserveAspectRatio="none">
        <path d="M0 0 H22 Q8 171 22 342 H0 Z" fill="#2f5fae"/>
        <path d="M22 0 Q8 171 22 342" stroke="#e8b531" stroke-width="2" fill="none"/>
      </svg>
      <span class="side-url">www.verant.co.uk</span>
      <div class="page-no" style="left:0">02</div>
      <div class="blk" style="left:46px;top:26px;width:200px">
        <h3><i class="icon"></i>WHO <span>WE ARE</span></h3>
        <p>We are a specialist team of investigators helping lenders, insolvency practitioners and solicitors locate assets and recover value for their clients across the UK and overseas.</p>
      </div>
      <div class="blk" style="left:270px;top:26px;width:200px">
        <h3><i class="icon"></i>WHAT <span>WE DO</span></h3>
        <p>We gather open source, registry and field intelligence into clear reports that show where assets sit, who controls them and how they may be recovered.</p>
      </div>
      <div class="blk" style="left:46px;top:170px;width:200px">
        <h3><i class="icon"></i>CASES:</h3>
        <p>Our work covers fraud, debt recovery, divorce disputes and insolvency matters, from single individuals to complex corporate groups.</p>
      </div>
      <div class="blk" style="left:270px;top:170px;width:200px">
        <h3><i class="icon"></i>FEES:</h3>
        <p>Fees are agreed at the outset and set by report tier, so clients know the cost before any work on the case begins.</p>
      </div>
    </article>
    <article class="page inner">
      <div class="blk" style="left:26px;top:20px;width:440px">
        <p class="brand" style="font-size:11px;margin-bottom:8px">VERANT</p>
        <h3>'MOSAIC' ASSET <span>TRACE REPORTS</span></h3>
        <p>Each report draws on many sources of information, pieced together to build a full picture of a subject's finances, property, companies and links to other people.</p>
        <p>Reports are written for clear decision making, with findings graded by confidence and sources listed for later evidence.</p>
        <div class="num"><b>1</b><span>Identity and address checks confirm the subject and their current whereabouts.</span></div>
        <div class="num"><b>2</b><span>Property, company and vehicle records reveal assets held directly or through others.</span></div>
        <div class="num"><b>3</b><span>Findings are summarised with recommended next steps for recovery action.</span></div>
      </div>
      <svg class="foot-band" viewBox="0 0 500 26" preserveAspectRatio="none">
        <rect width="500" height="26" fill="#2f5fae"/><rect width="500" height="2" fill="#e8b531"/>
      </svg>
      <span class="foot-url">www.verant.co.uk</span>
      <div class="page-no" style="left:0">03</div>
    </article>
  </div>
</section>

<!-- Stage 4: inner spread, tiers and director -->
<section class="stage">
  <div class="spread">
    <article class="page inner">
      <p class="brand" style="position:absolute;right:20px;top:14px;font-size:9px">VERANT</p>
      <table class="tier-table">
        <thead><tr><th>Report Tier</th><th>Basic Search</th><th>Standard Trace</th><th>Enhanced Trace</th></tr></thead>
        <tbody>
          <tr><td>Identity checks</td><td>Name and address</td><td class="shade2">Full identity profile</td><td class="shade">Profile with associates</td></tr>
          <tr><td>Property</td><td>Land registry</td><td class="shade2">UK property holdings</td><td class="shade">UK and overseas</td></tr>
          <tr><td>Companies</td><td>Directorships</td><td class="shade2">Shareholdings</td><td class="shade">Group structures</td></tr>
          <tr><td>Turnaround</td><td>5 days</td><td class="shade2">10 days</td><td class="shade">15 days</td></tr>
        </tbody>
        <tfoot><tr><td>Price</td><td>Fixed</td><td>Fixed</td><td>Quoted</td></tr></tfoot>
      </table>
      <svg class="foot-band" viewBox="0 0 500 26" preserveAspectRatio="none">
        <rect width="500" height="26" fill="#2f5fae"/><rect width="500" height="2" fill="#e8b531"/>
      </svg>
      <span class="foot-url" style="left:18px;right:auto">www.verant.co.uk</span>
    </article>
    <article class="page inner">
      <div class="blk" style="left:26px;top:20px;width:210px">
        <p class="brand" style="font-size:9px;margin-bottom:10px">VERANT</p>
        <h3>'OSINT' <span>TIER</span></h3>
        <p>Our open source tier searches public records, media and online platforms to locate a subject and identify assets quickly and at low cost.</p>
        <p>It suits early stage cases where a client needs to judge whether fuller tracing work is worth the spend.</p>
        <p>Results are delivered in a short written summary with links to every source used.</p>
      </div>
      <div class="blk" style="left:270px;top:30px;width:200px">
        <h3>DIRECTOR OF <span>ASSET TRACING</span></h3>
      </div>
      <div class="portrait" role="img" aria-label="Portrait photograph of the director"></div>
      <div class="blk" style="left:332px;top:66px;width:140px">
        <h3>DAN MERCER -</h3>
        <p>Chief Investigator and Director</p>
      </div>
      <div class="blk" style="left:270px;top:134px;width:200px">
        <p>Dan has led asset tracing work for over fifteen years, advising banks, law firms and insolvency teams on complex recovery cases at home and abroad.</p>
      </div>
      <svg class="foot-band" viewBox="0 0 500 26" preserveAspectRatio="none">
        <rect width="500" height="26" fill="#2f5fae"/><rect width="500" height="2" fill="#e8b531"/>
      </svg>
      <span class="foot-url">www.verant.co.uk</span>
      <div class="page-no" style="left:0">04</div>
    </article>
  </div>
</section>

</body>
</html>
```